I need some graphic design. For business card and price tag , my company name is VIRO , color: rose gold & off white.

I need professional and luxury design for

*Business card L: 5.5cm W:8.5 cm
*Price tag (I don't have specific sizes now)
*Envelope for invoices length: 15 cm + width 9cm

Color of the business: Rose gold code #CC9966+ Off white.

I want it luxury. My business name is VIRO. I attach the logo and the type of my style I Like.

_______________________________________________
Details for Business Card:

العنوان: الكويت ، شرق، شارع البحراوي برج الظفرة ميزانين٢
Address: kuwait city - sharq- Bahrawi street- Dhafra Tower M2.
Telephone: +965-55024937
Email: [login to view URL]@[login to view URL]

```html
<!DOCTYPE html>
<html lang="en">
<head>
<meta charset="utf-8">
<title>VIRO Business Card</title>
<link rel="stylesheet" href="https://fonts.googleapis.com/css2?family=Amiri:wght@400&display=swap">
<style>
  :root {
    --rose-gold: #c8876a;
    --off-white: #fdfcfa;
    --stage: #d4d4d4;
    --marble-light: #f4f4f3;
    --marble-mid: #e2e2e1;
    --marble-vein: #cfd0d0;
    --card-shadow: rgba(0, 0, 0, 0.18);
  }
  * { margin: 0; padding: 0; box-sizing: border-box; }
  html, body {
    width: 1200px;
    height: 960px;
    overflow: hidden;
    background: var(--stage);
  }
  .sheet {
    width: 1200px;
    height: 960px;
    display: flex;
    flex-direction: column;
    align-items: center;
    justify-content: center;
    gap: 40px;
  }
  .card {
    width: 660px;
    height: 427px;
    background: var(--off-white);
    box-shadow: 0 6px 18px var(--card-shadow);
    position: relative;
  }
  .card-front {
    display: flex;
    flex-direction: column;
    align-items: center;
    color: var(--rose-gold);
    font-family: "Amiri", "Times New Roman", serif;
    font-weight: 400;
  }
  .brand-name {
    margin-top: 84px;
    font-size: 64px;
    font-weight: 400;
    letter-spacing: 0.02em;
    line-height: 1;
  }
  .address-ar {
    margin-top: 64px;
    font-size: 22px;
    line-height: 1.2;
    direction: rtl;
  }
  .address-en {
    margin-top: 6px;
    font-size: 21px;
    line-height: 1.2;
  }
  .contact-icons {
    margin-top: 14px;
    display: flex;
    gap: 8px;
  }
  .contact-icons svg {
    width: 22px;
    height: 22px;
  }
  .phone {
    margin-top: 6px;
    font-size: 20px;
    line-height: 1.2;
  }
  .email {
    margin-top: 4px;
    font-size: 20px;
    line-height: 1.2;
  }
  .card-back {
    background:
      radial-gradient(ellipse at 30% 25%, var(--marble-light) 0%, transparent 60%),
      linear-gradient(160deg, var(--marble-light) 0%, var(--marble-mid) 35%, var(--marble-light) 55%, var(--marble-vein) 80%, var(--marble-light) 100%);
  }
</style>
</head>
<body>
<main class="sheet">
  <section class="card card-front">
    <h1 class="brand-name">VIRO</h1>
    <p class="address-ar" lang="ar">الكويت، شرق، شارع البحراوي برج الظفرة ميزانين٢</p>
    <p class="address-en">Kuwait City, Sharq-Bahrawi Street, Dhafra Tower M2</p>
    <div class="contact-icons">
      <svg viewBox="0 0 24 24" aria-label="Phone">
        <circle cx="12" cy="12" r="10.5" fill="none" stroke="currentColor" stroke-width="1.5"/>
        <path d="M8.6 7.2c.4-.4 1-.4 1.3 0l1 1.3c.3.4.2.9-.1 1.2l-.6.6c.5 1.2 1.4 2.1 2.6 2.6l.6-.6c.3-.3.8-.4 1.2-.1l1.3 1c.4.3.4.9 0 1.3l-.7.7c-.6.6-1.5.7-2.3.3-2.1-1-3.7-2.6-4.7-4.7-.4-.8-.3-1.700.3-2.3z" fill="currentColor"/>
      </svg>
      <svg viewBox="0 0 24 24" aria-label="Mobile">
        <circle cx="12" cy="12" r="10.5" fill="none" stroke="currentColor" stroke-width="1.5"/>
        <rect x="8.7" y="6" width="6.6" height="12" rx="1.2" fill="none" stroke="currentColor" stroke-width="1.4"/>
        <circle cx="12" cy="15.8" r="0.8" fill="currentColor"/>
      </svg>
    </div>
    <p class="phone">+965-55024937</p>
    <p class="email">hello@viro-kw.com</p>
  </section>

  <section class="card card-back" role="img" aria-label="White marble surface with a rose gold geometric line pattern"></section>
</main>
</body>
</html>
```